New young doctors office business card

Doctor's office
Hello:
My name is Dr. Mateo Anselmo Quiroga Benítez. I need a business card for my new office located within a hospital. The name of the hospital is "Hospital Almendral". Although the hospital logo and name must be included in the business card, please make me a personal logo for myself. The logo might be maybe my name in a stylish font, or my initials (MAQB) or something like that. Im more inclined to a font logo, rather than a image logo, but a good one might change my mind. The info on my business card is going to be in spanish. The following info must be included please (the info within parenthesis is not to be included, it is provided for you to understand it since it's in spanish, so you can properly place it on the card):
-Dr. Mateo Anselmo Quiroga Benítez (my name)
-Medicina general (My specialty)
-Hospital Almendral (The name of the hospital where my office is)
-Calle Tomás Ibarrola #527 Col. Peñascal (address)
-Tel 471-5836 (Office phone)
-Sábado y domingo 10:00 am a 10:00pm (Office hours)
-Emergencias: 613-907-5148 (Emergency phone)
-mateoqb@correoandino.net (email)
-English Spoken
So, that's all the info i need to be on the business card. Although it's a business card for a doctor's office, i dont want it to be a boring, plain business card. Make it eye-catchy and stylish please. As i said, the hospital logo must be included. You'll find it on the heading of the PDF file i attached, but dont make it the center of attention.
Physician
Hello:My name is Dr. Mateo Anselmo Quiroga Benítez. I need a business card for my new office located within a hospital. The name of the hospital is "Hospital Almendral". Although the hospital logo and name must be included in the business card, please make me a personal logo for myself. The logo might be maybe my name in a stylish font, or my initials (MAQB) or something like that. Im more inclined to a font logo, rather than a image logo, but a good one might change my mind. The info on my business card is going to be in spanish. The following info must be included please (the info within parenthesis is not to be included, it is provided for you to understand it since it's in spanish, so you can properly place it on the card):-Dr. Mateo Anselmo Quiroga Benítez (my name)-Medicina general (My specialty)-Hospital Almendral (The name of the hospital where my office is)-Calle Tomás Ibarrola #527 Col. Peñascal (address)-Tel 471-5836 (Office phone)-Sábado y domingo 10:00 am a 10:00pm (Office hours)-Emergencias: 613-907-5148 (Emergency phone)-mateoqb@correoandino.net (email)-English Spoken So, that's all the info i need to be on the business card. Although it's a business card for a doctor's office, i dont want it to be a boring, plain business card. Make it eye-catchy and stylish please. As i said, the hospital logo must be included. You'll find it on the heading of the PDF file i attached, but dont make it the center of attention.

```html
<!DOCTYPE html>
<html lang="es">
<head>
<meta charset="utf-8">
<title>Tarjeta de presentación — Dr. Mateo Anselmo Quiroga Benítez</title>
<link href="https://fonts.googleapis.com/css2?family=Nunito:wght@700;800&family=Quicksand:wght@500;600;700&family=Roboto+Condensed:wght@500&display=swap" rel="stylesheet">
<style>
  :root {
    --navy: #26388a;
    --navy-deep: #1f2f78;
    --ink: #2a2a2e;
    --paper: #ffffff;
    --backdrop: #e6e7ea;
    --watermark: rgba(38, 56, 138, 0.07);
  }
  * { box-sizing: border-box; margin: 0; padding: 0; }
  html, body { width: 1200px; height: 1200px; overflow: hidden; }
  body {
    background: var(--backdrop);
    font-family: "Quicksand", sans-serif;
    color: var(--ink);
    position: relative;
  }
  .card {
    position: absolute;
    width: 840px;
    height: 480px;
    background: var(--paper);
    box-shadow: 0 18px 40px rgba(0,0,0,0.18);
    overflow: hidden;
  }
  .card__band {
    position: absolute;
    left: 0; right: 0; bottom: 0;
    height: 30px;
    background: var(--navy);
  }

  /* Front */
  .card--front { left: 150px; top: 90px; }
  .hospital-mark {
    position: absolute;
    left: 80px; top: 196px;
    display: flex; align-items: center; gap: 12px;
  }
  .hospital-mark__square {
    width: 22px; height: 22px; background: var(--navy); flex: none;
  }
  .hospital-mark__name {
    font-family: "Quicksand", sans-serif;
    font-weight: 700;
    font-size: 22px;
    letter-spacing: 1px;
    color: var(--navy);
    white-space: nowrap;
  }
  .front-divider {
    position: absolute;
    left: 418px; top: 178px;
    width: 4px; height: 58px;
    background: var(--navy);
  }
  .front-contact {
    position: absolute;
    left: 440px; top: 176px;
    list-style: none;
    color: var(--navy);
  }
  .front-contact li { display: flex; align-items: center; gap: 12px; height: 30px; white-space: nowrap; }
  .front-contact svg { width: 20px; height: 20px; fill: var(--navy); flex: none; }
  .front-contact__phone { font-family: "Quicksand", sans-serif; font-weight: 700; font-size: 24px; line-height: 30px; }
  .front-contact__address { font-family: "Roboto Condensed", sans-serif; font-weight: 500; font-size: 17px; line-height: 30px; }

  /* Back */
  .card--back { left: 230px; top: 630px; }
  .card__watermark {
    position: absolute;
    left: 560px; top: 150px;
    width: 220px; height: 210px;
    background: var(--watermark);
  }
  .doctor {
    position: absolute;
    left: 60px; top: 70px;
  }
  .doctor__name {
    font-family: "Nunito", sans-serif;
    font-weight: 800;
    font-size: 33px;
    color: var(--navy);
    letter-spacing: -0.3px;
    white-space: nowrap;
  }
  .doctor__role {
    font-family: "Quicksand", sans-serif;
    font-weight: 600;
    font-size: 22px;
    color: var(--ink);
    margin-top: 2px;
  }
  .details {
    position: absolute;
    left: 80px; top: 200px;
    display: flex;
  }
  .details__rail {
    width: 34px;
    background: var(--navy);
    display: flex; flex-direction: column; align-items: center;
    padding-top: 8px;
  }
  .details__rail svg { width: 20px; height: 20px; margin: 7px 0; fill: none; stroke: #fff; stroke-width: 2; }
  .details__rail svg.solid { fill: #fff; stroke: none; }
  .details__list {
    list-style: none;
    padding-left: 18px;
    font-size: 19px;
    font-weight: 500;
  }
  .details__list li { height: 34px; line-height: 34px; white-space: nowrap; }
  .details__list strong { font-weight: 700; }
</style>
</head>
<body>

<section class="card card--front">
  <div class="hospital-mark">
    <span class="hospital-mark__square"></span>
    <span class="hospital-mark__name">HOSPITAL ALMENDRAL</span>
  </div>
  <span class="front-divider"></span>
  <ul class="front-contact">
    <li>
      <svg viewBox="0 0 24 24"><path d="M3 9c0-3 4-5 9-5s9 2 9 5v2h-5V9c-1-.6-2.5-1-4-1s-3 .4-4 1v2H3z"/><path d="M6 12h12l2 8H4z"/><circle cx="12" cy="16" r="2.2" fill="#fff"/></svg>
      <span class="front-contact__phone">471-5836</span>
    </li>
    <li>
      <svg viewBox="0 0 24 24"><path d="M12 3 2 12h3v8h5v-5h4v5h5v-8h3z"/></svg>
      <span class="front-contact__address">Calle Tomás Ibarrola #527 Col. Peñascal</span>
    </li>
  </ul>
  <div class="card__band"></div>
</section>

<section class="card card--back">
  <div class="card__watermark"></div>
  <header class="doctor">
    <h1 class="doctor__name">Dr. Mateo Anselmo Quiroga Benítez</h1>
    <p class="doctor__role">Medicina general | Hospital Almendral</p>
  </header>
  <div class="details">
    <div class="details__rail">
      <svg class="solid" viewBox="0 0 24 24"><path d="M12 2a7 7 0 0 0-7 7c0 5 7 13 7 13s7-8 7-13a7 7 0 0 0-7-7zm0 9.5A2.5 2.5 0 1 1 12 6.5a2.5 2.5 0 0 1 0 5z"/></svg>
      <svg viewBox="0 0 24 24"><path d="M6 3h4l1.5 5-2.5 1.5a11 11 0 0 0 5.5 5.5l1.5-2.5 5 1.5v4a2 2 0 0 1-2 2A17 17 0 0 1 4 5a2 2 0 0 1 2-2z"/></svg>
      <svg class="solid" viewBox="0 0 24 24"><path d="M3 9c0-3 4-5 9-5s9 2 9 5v2h-5V9c-1-.6-2.5-1-4-1s-3 .4-4 1v2H3z"/><path d="M6 12h12l2 8H4z"/></svg>
      <svg viewBox="0 0 24 24"><rect x="3" y="6" width="18" height="12"/><path d="m3 6 9 7 9-7"/></svg>
      <svg viewBox="0 0 24 24"><circle cx="12" cy="12" r="9"/><path d="M12 7v5l3 2"/></svg>
      <svg viewBox="0 0 24 24"><circle cx="12" cy="12" r="9"/><path d="m8 8 9 4-9 4 2-4z"/></svg>
    </div>
    <ul class="details__list">
      <li>Calle Tomás Ibarrola #527 Col. Peñascal</li>
      <li>471-5836 (Office phone)</li>
      <li>613-907-5148 (Emergency phone)</li>
      <li>mateoqb@correoandino.net</li>
      <li>Sábado y domingo 10:00 am a 10:00pm <strong>(Office hours)</strong></li>
      <li>English Spoken</li>
    </ul>
  </div>
  <div class="card__band"></div>
</section>

</body>
</html>
```